SofaVoyager ClipStream page redesign needed

SofaVoyager specializes in static, long play, ambient, experiential videos that allow viewers to vicariously enjoy the sights and sounds of fascinating locations around the world. The channel lets you enjoy the sights and sounds of beaches, markets, European cafes, fountains, skylines, train stations, etc. The SofaVoyager library consists of over 3,000 travel videos from around the world that are broadcast n television and shown on PearView and Zibo, but we need to improve our ClipStream presence-- and we need your help. Can you help us design a new ClipStream channel @sofavoyager that borrows the best features from other 4K travel video channels? We want to begin offering dozens of 8-hour videos with different background sounds for viewers: natural sound, brown noise, piano classical music and jazz. Can you help us become one of the top ambient channels on ClipStream?

Visit here to learn more:
http://sofavoyager.example
https://www.instagram.example/sofavoyager/
https://www.facebook.example/sofavoyager

Keywords: travel, ambient, 4K, cafe, study, brown noise, white noise, relaxing, work and study, jazz, focus, chill, piano, nature, slow television

Hoping to get some more creative designs.

Here are 2,100 videos that will be on the ClipStream channel. Please use still images from these actual videos for the ClipStream page. https://vimeo.example/sofavoyager

```html
<!DOCTYPE html>
<html lang="en">
<head>
<meta charset="utf-8">
<title>SofaVoyager Channel Banner</title>
<link rel="stylesheet" href="https://fonts.googleapis.com/css2?family=Poppins:wght@500;600;700&family=Libre+Baskerville&family=Barlow+Condensed:wght@700&display=swap">
<style>
  :root {
    --ink: #0b0b0b;
    --paper: #e4e4e4;
    --paper-shade: #d9d9d9;
    --accent: #d0142c;
    --white: #ffffff;
    --text: #1a1a1a;
  }
  * { margin: 0; padding: 0; box-sizing: border-box; }
  html, body { width: 1200px; height: 209px; overflow: hidden; background: var(--ink); }
  .banner { position: relative; width: 1200px; height: 209px; background: var(--ink); overflow: hidden; }
  .banner__paper { position: absolute; inset: 0; }
  .postcard { position: absolute; left: 0; top: 0; }

  .tagline {
    position: absolute;
    left: 286px; top: 56px;
    background: var(--ink);
    color: var(--white);
    font-family: "Libre Baskerville", Georgia, serif;
    font-size: 13px;
    letter-spacing: 3.2px;
    line-height: 17px;
    padding: 1px 10px 0 12px;
    transform: rotate(-4deg);
    transform-origin: left center;
    white-space: nowrap;
  }
  .subline {
    position: absolute;
    left: 380px; top: 84px;
    background: var(--accent);
    color: var(--white);
    font-family: "Barlow Condensed", "Arial Narrow", sans-serif;
    font-weight: 700;
    font-size: 11.5px;
    letter-spacing: 0.2px;
    line-height: 19px;
    padding: 0 9px 0 10px;
    transform: rotate(-2.5deg);
    transform-origin: left center;
    white-space: nowrap;
  }
  .intro {
    position: absolute;
    left: 285px; top: 122px;
    width: 328px;
    font-family: "Poppins", Arial, sans-serif;
    font-weight: 500;
    font-size: 10.6px;
    line-height: 17.4px;
    color: var(--text);
    text-align: justify;
  }
  .intro__lead { color: var(--accent); font-weight: 600; font-size: 12px; }

  .brand { position: absolute; left: 692px; top: 58px; display: flex; align-items: center; height: 110px; }
  .brand__mark { width: 106px; height: 106px; border-radius: 50%; border: 11px solid var(--ink); background: var(--white); flex: none; }
  .brand__name {
    margin-left: 24px;
    font-family: "Poppins", Arial, sans-serif;
    font-weight: 700;
    font-size: 52px;
    letter-spacing: -1.5px;
    color: var(--ink);
    line-height: 1;
  }
</style>
</head>
<body>
<div class="banner">
  <svg class="banner__paper" width="1200" height="209" viewBox="0 0 1200 209" aria-hidden="true">
    <path fill="var(--paper)" d="M8 7 H808 L816 9 L826 12 L838 14 L850 15 L864 18 L880 20 L896 22 L914 23 L930 26 L948 27 L966 29 L984 30 L1000 31 L1016 28 L1030 31 L1048 30 L1066 32 L1084 31 L1102 33 L1120 32 L1140 34 L1160 33 L1178 35 L1192 34 V202 H820 L812 198 L800 196 L786 197 L770 195 L752 196 L736 194 L718 195 L700 193 L680 194 L660 192 L640 193 L620 191 L600 192 L580 190 L560 191 L540 190 L520 192 L500 191 L480 193 L460 192 L440 194 L420 196 L400 195 L384 198 L368 199 L352 202 H8 Z"/>
  </svg>

  <svg class="postcard" width="300" height="209" viewBox="0 0 300 209">
    <defs>
      <linearGradient id="cityscape" x1="0" y1="0" x2="0" y2="1">
        <stop offset="0" stop-color="#7fa6d6"/>
        <stop offset="0.45" stop-color="#a9b9c6"/>
        <stop offset="0.65" stop-color="#5f7a4a"/>
        <stop offset="1" stop-color="#2f5a2a"/>
      </linearGradient>
    </defs>
    <g transform="rotate(-11 149 109)">
      <rect x="45" y="50" width="208" height="118" fill="var(--white)"/>
      <rect x="50" y="55" width="198" height="108" fill="url(#cityscape)" role="img" aria-label="Photo of a city skyline with cathedral towers, a volcano and green trees"/>
    </g>
  </svg>

  <div class="tagline">WHERE IN THE WORLD?</div>
  <div class="subline">PARTY OUT WITH US FOR THREE DAYS!</div>

  <p class="intro"><span class="intro__lead">Lorem ipsum dolor sit amet</span> consectetur adipisicing elit, sed do ei usmod tempor incididunt ut labore et dolore magna aliqua. Ut enim ad minim veniam.</p>

  <div class="brand">
    <div class="brand__mark"></div>
    <div class="brand__name">SofaVoyager</div>
  </div>
</div>
</body>
</html>
```